Web site for Physical Therapy Clinic

Looking for a web designer who has experience in planning & designing graphic user interfaces for web site.
You will be delivered a sitemap/flow diagram and a general visual concept and expected to deliver finished web GUI design in PSD (or any suitable) format.
RESPONSIBILITIES:
-Interpreting the sitemap/flow diagram into an user interface
-Developing a visual concept which aligns with the brands and project goals
-Building wireframes
-Design usable, technically feasible, great looking user interfaces in Photoshop(or Illustrator)
-Present your design in jpg format
-Delivering pixel perfect design ready to be converted to html/css
EXPECTATIONS:
-Adobe Creative Suite
-Deliver quality design by applying sound design practices with solid methodology, workflow & discipline.
-Manage the design process from start to finish, including gathering requirements and delivering final assets
-Strong sense of design and knowledge of typography, grid systems, color theory, usability, interactivity and information architecture principles
-Familiar with HTML, CSS, and JavaScript knowledge for optimizing design concepts around these technologies
-Familiar with standards-based, cross-browser, multi-device design
-Familiar with responsive web design/development
-Participate in estimating project efforts and delivery timelines
-Identify technical, schedule, and other project risks and provide relevant feedback
-Proactively collaborate and communicate
-Ability to multitask and prioritize multiple concurrent assignments
-High attention to detail
Veltora Physical Therapy provides personalized and high-quality therapy services. Patients are treated in two different settings; at our outpatient clinic or through home health visits. The services we provide are: Physical Therapy, Occupational Therapy, Speech Therapy and Massage Therapy.
We are looking for a designer/developer to build a fully-functional website for our business. The website needs to be:
• Fast-loading
• Mobile-compatible
• User-friendly
The following web address has been secured through hostquarry.example:
www.veltorapt.example
Tabs for the website will include...
Home
About
• History
• Team
Patients
• Services
• Insurances & payments accepted
• Coverage areas
Agencies
• Inquiries
• Forms & credentials
• Coverage areas
Therapists
• Reasons to work with us
• Career opportunities
• Application
FAQ
Contact
• Inquiries
• Locations
Breakdown of content needed on each page:
HOME
• Tagline
ABOUT
• History
• Team
PATIENTS
• Pain Management
- Neck & back pain
- Radiculopathy
- Sacroiliac Joint Syndrome
- Status Post Laminectomy
- Status Post Spinal Fusion
- Patellafemoral pain
- Arthritis: Osteoarthritis & Rheumatoid Arthritis
- Temporomandibular Joint
- Post-amputation
• Neurological Disorders
- Cerebral Vascular Accidents
- Parkinson's disease
- Multiple Sclerosis
- Traumatic & non-traumatic Brain Injury
- Spinal cord injury
- Guillain Barre
- Intracranial hemorrhage
- Diabetic neuropathy
- Post Polio Syndrome
• Work/Sport Injuries
- Carpal Tunnel Syndrome
- Disc Hernia
- Plantar Fasciitis
- Sciatica
- Frozen Shoulder
- Rotator Cuff injury/surgery
- Hip surgery
- Knee surgery: Anterior/Posterior Cruciate Ligament & Meniscal Tear
- Ankle sprain
- Tennis Elbow
- Golfer's Elbow
• Services
- Outpatient
- Home Health (with coverage area maps)
• Languages
- English
- Spanish
- Vietnamese
- Farsi
- Mandarin
- Tagalog
• Insurances Accepted
- HMO
- PPO
- Medicare
- Workers Compensation
• Physician Referral Form (printable PDF)
• Patient Registration Form (able to sign and print)
AGENCIES
• Physical Therapy Coverage Areas with map
• Occupational Therapy Coverage Areas with map
• Speech Therapy Coverage Areas with map
• Inquiry Form that goes directly to Veltora email
- Name
- Title
- Company
- Phone Number
- Email
- Question
• Password access to Credentials & Contact List (editable)
THERAPISTS
• Reasons to work with us
- check example (http://www.kinarelpt.example/#!therapists/q48zt)
- add Referral Bonus
• Career Opportunities editable through an excel worksheet
• Application form that goes directly to Veltora email
- check example (http://www.kinarelpt.example/#!therapist-application-/vm2k)
FAQ
CONTACT
• Inquiry form
- option of "Agency" or "Patient"
- option of "Home Health Services" or "Outpatient Clinic"
- Question
• Clinic Location & Hours
30587 Marwood St., Suite F
Garden Grove, CA 92843
Monday - Friday 8am - 5pm
• Home Health Office Hours
Monday - Friday 8:30am - 5:30pm
• Connect to social networks
- Linkedin
https://www.linkedin.example/profile/view?id=518093647&authType=NAME_SEARCH&authToken=qrLm&locale=en_US&trk=tyah&trkInfo=tarId%3A1538204716529%2Ctas%3Aveltora%20physical%20%2Cidx%3A1-1-1
- Facebook
https://www.facebook.example/pages/Veltora-Physical-Therapy/587120964318
Adult patients ages 18 to 80 in need of pain management and/or rehab. Home health agencies that contract therapists.
Architecture

```html
<!DOCTYPE html>
<html lang="en">
<head>
<meta charset="utf-8">
<title>Veltora Physical Therapy</title>
<link rel="stylesheet" href="https://fonts.googleapis.com/css2?family=Lato:wght@400;700&family=Hind:wght@400;500&display=swap">
<style>
  :root{
    --red-deep:#5a0306;
    --red-mid:#9b0b10;
    --maroon:#880a10;
    --nav-blue:#17198a;
    --panel-blue:#1a4c9c;
    --button-blue:#1d4f9e;
    --ink:#2b2b2b;
    --text:#444;
    --grey-band:#e2e2e2;
    --welcome-bg:#f4f4f4;
    --white:#fff;
    --rule:#d6d6d6;
  }
  *{box-sizing:border-box;margin:0;padding:0}
  html,body{width:1200px;height:2757px;overflow:hidden}
  body{position:relative;background:var(--white);font-family:"Hind","Lato",sans-serif;color:var(--ink)}
  .abs{position:absolute}

  /* Header band */
  .top-band{left:0;top:0;width:1200px;height:747px;
    background:radial-gradient(ellipse at 50% 45%,var(--red-mid) 0%,#7d070b 55%,var(--red-deep) 100%)}
  .logo-bar{left:112px;top:66px;width:977px;height:111px;background:var(--white)}
  .logo{left:22px;top:24px;display:flex;align-items:center;gap:12px;color:var(--maroon);
    font-family:"Lato",sans-serif;font-weight:700;line-height:1}
  .logo-mark{width:18px;height:18px;background:var(--maroon)}
  .logo-name{font-size:30px;letter-spacing:1px}
  .logo-name small{display:block;font-size:17px;letter-spacing:2px;margin-top:6px}
  .main-nav{left:112px;top:177px;width:977px;height:70px;background:var(--nav-blue);
    display:flex;align-items:center;padding-left:44px;gap:33px}
  .main-nav a{color:var(--white);text-decoration:none;font-size:19px;font-weight:500;letter-spacing:.3px;padding-top:4px}

  .hero{left:112px;top:247px;width:977px;height:441px;
    background:linear-gradient(120deg,#3a3a3a 0%,#c9a48c 35%,#e6d3c4 60%,#f1eeea 100%);
    box-shadow:0 26px 30px -12px rgba(0,0,0,.55)}
  .hero-card{left:620px;top:33px;width:307px;height:375px;background:rgba(34,34,34,.9);padding:28px 20px 0 20px;color:var(--white)}
  .hero-card h1{font-weight:400;font-size:46px;line-height:1;letter-spacing:1px}
  .hero-card .sub{font-size:17px;letter-spacing:3.4px;margin-top:4px}
  .hero-card p{font-size:15px;line-height:24px;margin-top:12px}
  .btn{display:inline-block;color:var(--white);text-decoration:none;font-size:15.5px;text-transform:uppercase;text-align:center;font-weight:500}
  .btn-blue{background:var(--button-blue);width:151px;height:46px;line-height:48px;margin-top:22px}
  .dots{left:17px;top:400px;display:flex;gap:11px}
  .dots span{width:11px;height:11px;border-radius:50%;background:var(--white)}
  .dots span.on{background:var(--nav-blue)}

  /* Settings */
  .settings{left:0;top:747px;width:1200px;height:421px;background:var(--grey-band)}
  .settings-lead{left:0;top:0;width:419px;height:421px;background:var(--panel-blue);color:var(--white);
    padding:80px 0 0 126px;font-size:41px;line-height:45px;text-transform:uppercase;font-weight:400}
  .setting{width:309px}
  .setting .photo{width:309px;height:184px}
  .setting h3{font-size:19px;font-weight:500;margin-top:22px;text-transform:uppercase}
  .setting p{font-size:13.5px;line-height:20px;color:var(--text);margin-top:6px}
  .btn-maroon{background:var(--maroon);height:39px;line-height:42px}
  .setting .btn{width:224px;margin-top:22px}

  /* Services */
  .section-title{width:1200px;left:0;text-align:center;font-size:32px;font-weight:400;color:#333;text-transform:uppercase}
  .service{width:226px;top:1313px}
  .service .photo{width:226px;height:147px}
  .service h3{font-size:15.5px;font-weight:500;text-transform:uppercase;margin-top:44px}
  .service p{font-size:13.5px;line-height:20px;color:var(--text);margin-top:18px}
  .service .btn{width:141px;margin-top:20px}

  /* Welcome */
  .welcome{left:0;top:1723px;width:1200px;height:719px;background:var(--welcome-bg)}
  .video{left:195px;top:125px;width:809px;height:431px;
    background:linear-gradient(100deg,#e7e2dc 0%,#c59a80 40%,#2c4a8a 62%,#d5c9bd 100%)}
  .play{left:346px;top:180px;width:118px;height:72px;border-radius:6px;background:rgba(30,30,30,.85)}
  .controls{left:115px;top:352px;width:580px;height:40px;border-radius:4px;background:rgba(30,30,30,.85)}
  .tagline{left:0;top:2307px;width:1200px;text-align:center;font-size:31px;line-height:41px;color:#333;font-weight:400}

  /* Footer */
  .foot-links{left:112px;top:2470px;list-style:none}
  .foot-links li{font-size:14.5px;line-height:31px}
  .foot-note{font-size:14.5px;color:var(--ink)}
  .address{font-size:14.5px;line-height:23px}
  .social{left:948px;top:2462px}
  .social-row{display:flex;align-items:center;height:48px}
  .social-row span{width:85px;font-size:14.5px}
  .social-row i{width:36px;height:36px;border:2px solid var(--panel-blue);border-radius:50%;display:block}
  .footer-rule{left:0;top:2701px;width:1200px;height:1px;background:var(--rule)}
  .copyright{left:0;top:2715px;width:1200px;text-align:center;font-size:14.5px}
</style>
</head>
<body>
  <div class="abs top-band"></div>

  <header class="abs logo-bar">
    <div class="abs logo"><span class="logo-mark"></span><span class="logo-name">VELTORA<small>PHYSICAL THERAPY</small></span></div>
  </header>

  <nav class="abs main-nav">
    <a>HOME</a><a>ABOUT</a><a>PATIENTS</a><a>AGENCIES/PHYSICIANS/CLIENTS</a><a>THERAPISTS</a><a>FAQ</a><a>CONTACT</a>
  </nav>

  <section class="abs hero" role="img" aria-label="Therapist's hands treating a patient's foot">
    <div class="abs hero-card">
      <h1>VELTORA</h1>
      <div class="sub">PHYSICAL THERAPHY</div>
      <p>Lorem Ipsum is simply dummy text of the printing and typesetting industry. Lorem Ipsum has been the industry's standard dummy text ever since the 1500s, when an unknown printer took a galley of type and scrambled it to make a type specimen book</p>
      <a class="btn btn-blue">Learn More</a>
    </div>
    <div class="abs dots"><span class="on"></span><span></span><span></span><span></span></div>
  </section>

  <section class="abs settings">
    <h2 class="abs settings-lead">Patients are treated in two different settings</h2>
    <article class="abs setting" style="left:445px;top:40px">
      <div class="photo" role="img" aria-label="Doctor consulting a patient at the clinic" style="background:linear-gradient(90deg,#f2f2f2,#d9c8bd 45%,#e9edf0)"></div>
      <h3>At our outpatient clinic</h3>
      <p>Lorem Ipsum is simply dummy text of the printing and typesetting industry. Lotrem Ipsum has been the industry's standard dummy text ever</p>
      <a class="btn btn-maroon">Make an appointment</a>
    </article>
    <article class="abs setting" style="left:779px;top:40px">
      <div class="photo" role="img" aria-label="Nurse assisting an elderly patient at home" style="background:linear-gradient(90deg,#e8e3dc,#2f5fa3 45%,#e6e1da)"></div>
      <h3>Through home health visits</h3>
      <p>Lorem Ipsum is simply dummy text of the printing and typesetting industry. Lotrem Ipsum has been the industry's standard dummy text ever</p>
      <a class="btn btn-maroon">Make an appointment</a>
    </article>
  </section>

  <h2 class="abs section-title" style="top:1238px">Our Services</h2>

  <article class="abs service" style="left:112px">
    <div class="photo" role="img" aria-label="Physical therapy session" style="background:linear-gradient(90deg,#e9e6e2,#c8473f 50%,#d8d2cc)"></div>
    <h3>Physical Therapy</h3>
    <p>Lorem Ipsum is simply dummy text of the printing and typesetting industry. Lotrem Ipsum has been the industry's standard dummy text ever</p>
    <a class="btn btn-maroon">Read More</a>
  </article>
  <article class="abs service" style="left:362px">
    <div class="photo" role="img" aria-label="Occupational therapy with exercise ball" style="background:linear-gradient(90deg,#3fa69a,#d9c24a 50%,#e6e0d8)"></div>
    <h3>Occupational Therapy</h3>
    <p>Lorem Ipsum is simply dummy text of the printing and typesetting industry. Lotrem Ipsum has been the industry's standard dummy text ever</p>
    <a class="btn btn-maroon">Read More</a>
  </article>
  <article class="abs service" style="left:612px">
    <div class="photo" role="img" aria-label="Speech therapy with a child" style="background:linear-gradient(90deg,#eeeeee,#6f86b6 50%,#efefef)"></div>
    <h3>Speech Therapy</h3>
    <p>Lorem Ipsum is simply dummy text of the printing and typesetting industry. Lotrem Ipsum has been the industry's standard dummy text ever</p>
    <a class="btn btn-maroon">Read More</a>
  </article>
  <article class="abs service" style="left:864px">
    <div class="photo" role="img" aria-label="Massage therapy session" style="background:linear-gradient(90deg,#c9733f,#eac0a0 50%,#f3e4d8)"></div>
    <h3>Massage Therapy</h3>
    <p>Lorem Ipsum is simply dummy text of the printing and typesetting industry. Lotrem Ipsum has been the industry's standard dummy text ever</p>
    <a class="btn btn-maroon">Read More</a>
  </article>

  <section class="abs welcome">
    <h2 class="abs section-title" style="top:44px">Welcome to Veltora Physical Theraphy</h2>
    <div class="abs video" role="img" aria-label="Video of a therapist examining a patient's knee">
      <div class="abs play">
        <svg width="118" height="72" viewBox="0 0 118 72"><polygon points="50,22 50,50 72,36" fill="#fff"/></svg>
      </div>
      <div class="abs controls">
        <svg width="580" height="40" viewBox="0 0 580 40">
          <rect x="12" y="16" width="430" height="8" fill="#555"/>
          <rect x="12" y="16" width="125" height="8" fill="#1e88d6"/>
          <rect x="460" y="14" width="40" height="12" fill="#1e88d6"/>
          <path d="M545 12l10 10M555 12l-10 10" stroke="#fff" stroke-width="2"/>
        </svg>
      </div>
    </div>
  </section>
  <p class="abs tagline">Veltora Physical Therapy provides personalised and<br>high-quality therapy services</p>

  <footer>
    <ul class="abs foot-links">
      <li>Home</li><li>About</li><li>Patients</li><li>Agencies/Physicians/Clients</li><li>Therapists</li><li>FAQ</li><li>Contact</li>
    </ul>
    <p class="abs foot-note" style="left:362px;top:2470px">Feature our address in the site</p>
    <address class="abs address" style="left:362px;top:2516px;font-style:normal">30587 Marwood St., Suite F<br>Garden Grove, CA 92843<br>Monday - Friday 8am - 5pm</address>
    <address class="abs address" style="left:612px;top:2516px;font-style:normal">4816 Larkmere Blvd., Suite B<br>Garden Grove, CA 92841<br>Monday - Friday 8:30am - 5:30pm</address>
    <div class="abs social">
      <div class="social-row"><span>Facebook</span><i></i></div>
      <div class="social-row"><span>Twitter</span><i></i></div>
      <div class="social-row"><span>Linkedin</span><i></i></div>
    </div>
    <div class="abs footer-rule"></div>
    <p class="abs copyright">© 2014 Company&nbsp; Name ,All Rights Reserved</p>
  </footer>
</body>
</html>
```